Flyer Vacation Gift Certificate

I need to create a beautiful flyer 8.5 x 11 PDF format flyer design. <br/><br/>Instructions:<br/>The flyer will really be a gift voucher for a las vegas vacation getaway. So must have a Las Vegas Theme exciting fun<br/><br/>The voucher should have two modules that will be editable. <br/>Must have a "Compliments Of" area and also must have an "Exclusively For" area<br/><br/>Keep in mind that this flyer will be printed so keep that in mind :)<br/><br/>Here the is the content for the vacation voucher:<br/><br/>There is no doubt that Las Vegas is one of the hottest travel destinations around the world. In fact, some people would even go as far as<br/>saying that perhaps it is THE hottest place to visit. Enjoy up to 4 nights of resort/casino accommodations in exciting Las Vegas, NV. Millions of people travel to this exciting city each year to enjoy its thrills. Thanks to the business you received this certificate from, now you can enjoy exciting Las Vegas, NV too!<br/><br/>Features:<br/>*Travel 7 Days A Week<br/>*Stay Your Choice Of Nights (1-4 Nights)<br/>*Good For Two Adults & Two Children<br/>*Pay Just The Taxes & Fees<br/>*Multiple Travel Date Requests Allowed<br/>*Fully Transferable To Another Person<br/>*Just A 30 Days Advance Notice Required<br/>*You Will Have 12 Months To Complete Travel After Redemption<br/><br/>HOW CAN WE DO THIS?<br/><br/>We contract with the world leading hotel chains and resorts to help them fill their otherwise empty rooms.<br/><br/>We help fill empty rooms which the hotels, resorts and cruise lines turn into additional revenue from other areas of their property and future bookings.<br/><br/>Hotels rarely experience full occupancy, yet they remain open, providing rooms and services at fixed costs. So when hotels give out their rooms by partnering with marketing companies like us, they might miss out on the room fee, but they already didn't have that in the first place, at least now they have the opportunity to gain a customer for their in-house restaurants, room service, their casinos, an extra day stay, future bookings, etc.<br/><br/>VIEW ALL THE DETAILS OF THIS SPECIAL OFFER AND REDEEM ONLINE AT <br/>WWW.TOPAZVOUCHERDESK.COM<br/><br/>Certificate ID # 47261-38504<br/>Expires 02/29/2020<br/><br/><br/>*terms and conditions apply see website for details<br/><br/>KEEP IN MIND THE EXAMPLES I AM UPLOADING ARE SIMPLY TO SHOW YOU THAT THEY CONTAIN THE "COMPLIMENTS OF" AND "EXCLUSIVELY FOR" ELEMENTS. THESE MUST BE INCLUDED IN NEW DESIGN. PLEASE ONLY USE THE CONTENT I PROVIDED IN BRIEF, DONT USE CONTENT FROM EXAMPLES.

Target Market(s)

CONSUMERS THAT HAVE BEEN REWARDED WITH A VACATION CERTIFICATE FOR DOING BUSINESS WITH A COMPANY.

COMPANIES USE THESE AS MARKETING INCENTIVES TO ATTRACT MORE CUSTOMERS AND TO REWARD LOYALTY, ETC.

Industry/Entity Type

Travel Industry

Colors

Designer to choose colors to be used in the design.

Requirements
Must have
• I need to create a beautiful flyer 8.5 x 11 PDF format flyer design.
• Instructions:
• The flyer will really be a gift voucher for a las vegas vacation getaway. So must have a Las Vegas Theme exciting fun
• The voucher should have two modules that will be editable.
• Must have a "Compliments Of" area and also must have an "Exclusively For" area
• Keep in mind that this flyer will be printed so keep that in mind :)
• Here the is the content for the vacation voucher:
• There is no doubt that Las Vegas is one of the hottest travel destinations around the world. In fact, some people would even go as far as
• saying that perhaps it is THE hottest place to visit. Enjoy up to 4 nights of resort/casino accommodations in exciting Las Vegas, NV. Millions of people travel to this exciting city each year to enjoy its thrills. Thanks to the business you received this certificate from, now you can enjoy exciting Las Vegas, NV too!
• Features:
• *Travel 7 Days A Week
• *Stay Your Choice Of Nights (1-4 Nights)
• *Good For Two Adults & Two Children
• *Pay Just The Taxes & Fees
• *Multiple Travel Date Requests Allowed
• *Fully Transferable To Another Person
• *Just A 30 Days Advance Notice Required
• *You Will Have 12 Months To Complete Travel After Redemption
• HOW CAN WE DO THIS?
• We contract with the world leading hotel chains and resorts to help them fill their otherwise empty rooms.
• We help fill empty rooms which the hotels, resorts and cruise lines turn into additional revenue from other areas of their property and future bookings.
• Hotels rarely experience full occupancy, yet they remain open, providing rooms and services at fixed costs. So when hotels give out their rooms by partnering with marketing companies like us, they might miss out on the room fee, but they already didn't have that in the first place, at least now they have the opportunity to gain a customer for their in-house restaurants, room service, their casinos, an extra day stay, future bookings, etc.
• VIEW ALL THE DETAILS OF THIS SPECIAL OFFER AND REDEEM ONLINE AT
• WWW.TOPAZVOUCHERDESK.COM
• Certificate ID # 47261-38504
• Expires 02/29/2020
• *terms and conditions apply see website for details
• KEEP IN MIND THE EXAMPLES I AM UPLOADING ARE SIMPLY TO SHOW YOU THAT THEY CONTAIN THE "COMPLIMENTS OF" AND "EXCLUSIVELY FOR" ELEMENTS. THESE MUST BE INCLUDED IN NEW DESIGN. PLEASE ONLY USE THE CONTENT I PROVIDED IN BRIEF, DONT USE CONTENT FROM EXAMPLES.
Nice to have
• EXCITING LAS VEGAS IMAGES THAT MAKE SOMEONE WANT TO GO THERE

```html
<!DOCTYPE html>
<html lang="en">
<head>
<meta charset="utf-8">
<title>Las Vegas Vacation Gift Certificate</title>
<link rel="stylesheet" href="https://fonts.googleapis.com/css2?family=Montserrat:wght@500;600;700;800;900&family=Russo+One&display=swap">
<style>
  :root{
    --page:#eceef0;
    --red:#e8192c;
    --gold:#ffd43a;
    --gold-light:#fff2a6;
    --gold-deep:#e8a10f;
    --white:#ffffff;
  }
  *{box-sizing:border-box;margin:0;padding:0}
  html,body{width:1200px;height:1200px;overflow:hidden}
  body{background:var(--page);font-family:"Montserrat",Arial,sans-serif;color:var(--white);position:relative}

  .flyer{
    position:absolute;left:150px;top:18px;width:900px;height:1164px;overflow:hidden;
    background:
      radial-gradient(ellipse 60% 40% at 80% 62%, rgba(120,20,40,.45), transparent 70%),
      radial-gradient(ellipse 50% 35% at 20% 70%, rgba(60,30,70,.4), transparent 70%),
      linear-gradient(180deg,#17121c 0%,#0d0b12 60%,#08070b 100%);
    box-shadow:0 10px 30px rgba(0,0,0,.25);
  }
  .hero{position:absolute;left:0;top:0;width:900px;height:530px;display:block}

  .offer-headline{position:absolute;left:21px;top:523px;width:560px}
  .offer-headline .lead{
    font-weight:800;font-size:22.5px;line-height:27px;text-transform:uppercase;
    color:var(--gold);letter-spacing:.2px;
  }
  .offer-headline .city{
    font-weight:900;font-size:53px;line-height:60px;margin-top:2px;letter-spacing:.5px;
    background:linear-gradient(180deg,var(--gold-light) 0%,var(--gold) 45%,var(--gold-deep) 100%);
    -webkit-background-clip:text;background-clip:text;color:transparent;
  }

  .exclusive{position:absolute;left:21px;top:644px;display:flex;align-items:flex-end;gap:6px}
  .exclusive .label{font-weight:700;font-size:26px;color:var(--red);text-transform:uppercase;line-height:30px}
  .exclusive .fill-line{width:282px;border-bottom:4px dotted var(--white);margin-bottom:5px}

  .intro{position:absolute;left:21px;top:683px;width:545px;font-size:11.6px;line-height:14.2px;font-weight:500}
  .intro p+p{margin-top:6px}
  .intro .highlight{color:var(--red)}

  .pill{
    position:absolute;height:21px;border-radius:11px;background:var(--red);
    font-family:"Russo One","Montserrat",sans-serif;font-size:15px;letter-spacing:1.8px;
    line-height:21px;text-transform:uppercase;padding:0 14px;color:var(--white);white-space:nowrap;
  }
  .pill.features-tag{left:29px;top:784px;width:128px;text-align:center}
  .pill.how-tag{left:22px;top:950px;width:260px;text-align:center}

  .features{position:absolute;left:21px;top:808px;list-style:none}
  .features li{display:flex;align-items:center;gap:9px;font-size:11.4px;font-weight:600;height:17.3px}
  .features svg{width:12px;height:12px;flex:none}

  .how-text{position:absolute;left:21px;top:978px;width:840px;font-size:11.3px;line-height:16px;font-weight:500}

  .compliments{position:absolute;left:588px;top:508px;width:285px;text-align:center}
  .compliments .label{font-weight:700;font-size:22px;line-height:30px;text-transform:uppercase;white-space:nowrap}
  .compliments .sponsor{margin-top:6px;font-weight:800;font-size:28px;line-height:40px;letter-spacing:-.3px;color:var(--white);white-space:nowrap}

  .recipient-box{
    position:absolute;left:603px;top:642px;width:255px;height:324px;border-radius:28px;
    background:var(--red);padding:6px;
  }
  .recipient-box .inner{position:relative;width:100%;height:100%;border:2px solid var(--white);border-radius:23px}
  .recipient-box .entry{position:absolute;left:21px;right:15px;border-bottom:3px dotted var(--white)}
  .recipient-box .entry.one{top:42px}
  .recipient-box .entry.two{top:94px}
  .recipient-box .entry.three{top:144px}
  .casino-art{
    position:absolute;left:14px;right:14px;bottom:8px;height:140px;border-radius:70px;
    background:radial-gradient(circle at 50% 50%,#2b2b2b 0%,#1a1a1a 22%,#b51218 24%,#f2f2f2 46%,rgba(255,255,255,.25) 62%,rgba(232,25,44,0) 75%);
  }

  .footer{
    position:absolute;left:0;bottom:0;width:900px;height:94px;background:var(--red);
    border-radius:22px 22px 0 0;padding:12px 24px 0 21px;
  }
  .footer .redeem{font-weight:600;font-size:14px;text-transform:uppercase;letter-spacing:0;white-space:nowrap}
  .footer .meta{display:flex;justify-content:space-between;align-items:flex-start;margin-top:10px}
  .footer .ids{font-weight:600;font-size:14px;line-height:18px}
  .footer .terms{font-size:9.6px;font-weight:500;margin-top:4px}
</style>
</head>
<body>
<main class="flyer">

  <svg class="hero" viewBox="0 0 900 530">
    <defs>
      <linearGradient id="nightSky" x1="0" y1="0" x2="0" y2="1">
        <stop offset="0" stop-color="#141238"/>
        <stop offset=".45" stop-color="#2a2373"/>
        <stop offset=".75" stop-color="#7a4a7d"/>
        <stop offset="1" stop-color="#e2a448"/>
      </linearGradient>
      <radialGradient id="signGlow" cx=".42" cy=".6" r=".45">
        <stop offset="0" stop-color="#fff6e0" stop-opacity=".85"/>
        <stop offset="1" stop-color="#fff6e0" stop-opacity="0"/>
      </radialGradient>
    </defs>
    <g role="img" aria-label="Night view of the Las Vegas Strip with the Welcome to Fabulous Las Vegas sign, a jet taking off, the Eiffel tower replica and a red gift ribbon">
      <path d="M0 0 H900 V378 Q450 636 0 382 Z" fill="url(#nightSky)"/>
      <path d="M0 0 H900 V378 Q450 636 0 382 Z" fill="url(#signGlow)"/>
    </g>
    <path d="M0 384 Q450 640 900 380" fill="none" stroke="#ffffff" stroke-width="3"/>
    <path d="M0 390 Q450 650 900 386" fill="none" stroke="var(--red)" stroke-width="8"/>
  </svg>

  <section class="offer-headline">
    <p class="lead">Enjoy up to 4 nights of resort<br>casino accommodations in exciting</p>
    <h1 class="city">LAS VEGAS, NV</h1>
  </section>

  <div class="exclusive">
    <span class="label">Exclusively for</span>
    <span class="fill-line"></span>
  </div>

  <section class="intro">
    <p>There is no doubt that Las Vegas is one of the hottest travel destinations around the world. In fact, some people would even go as far as saying that perhaps it is THE hottest place to visit.</p>
    <p><span class="highlight">Enjoy up to 4 nights of resort/casino accommodations in exciting Las Vegas, NV.</span> Millions of people travel to this exciting city each year to enjoy its thrills. Thanks to the business you received this certificate from, now you can enjoy exciting Las Vegas, NV too!</p>
  </section>

  <div class="pill features-tag">Features</div>
  <ul class="features">
    <li><svg viewBox="0 0 12 12"><rect x="1" y="2" width="9" height="9" fill="none" stroke="var(--red)" stroke-width="1.4"/><path d="M3 6 L5.3 8.4 L11 1.5" fill="none" stroke="var(--red)" stroke-width="1.6"/></svg>Travel 7 Days A Week</li>
    <li><svg viewBox="0 0 12 12"><rect x="1" y="2" width="9" height="9" fill="none" stroke="var(--red)" stroke-width="1.4"/><path d="M3 6 L5.3 8.4 L11 1.5" fill="none" stroke="var(--red)" stroke-width="1.6"/></svg>Stay Your Choice Of Nights (1-4 Nights)</li>
    <li><svg viewBox="0 0 12 12"><rect x="1" y="2" width="9" height="9" fill="none" stroke="var(--red)" stroke-width="1.4"/><path d="M3 6 L5.3 8.4 L11 1.5" fill="none" stroke="var(--red)" stroke-width="1.6"/></svg>Good For Two Adults &amp; Two Children</li>
    <li><svg viewBox="0 0 12 12"><rect x="1" y="2" width="9" height="9" fill="none" stroke="var(--red)" stroke-width="1.4"/><path d="M3 6 L5.3 8.4 L11 1.5" fill="none" stroke="var(--red)" stroke-width="1.6"/></svg>Pay Just The Taxes &amp; Fees</li>
    <li><svg viewBox="0 0 12 12"><rect x="1" y="2" width="9" height="9" fill="none" stroke="var(--red)" stroke-width="1.4"/><path d="M3 6 L5.3 8.4 L11 1.5" fill="none" stroke="var(--red)" stroke-width="1.6"/></svg>Multiple Travel Date Requests Allowed</li>
    <li><svg viewBox="0 0 12 12"><rect x="1" y="2" width="9" height="9" fill="none" stroke="var(--red)" stroke-width="1.4"/><path d="M3 6 L5.3 8.4 L11 1.5" fill="none" stroke="var(--red)" stroke-width="1.6"/></svg>Fully Transferable To Another Person</li>
    <li><svg viewBox="0 0 12 12"><rect x="1" y="2" width="9" height="9" fill="none" stroke="var(--red)" stroke-width="1.4"/><path d="M3 6 L5.3 8.4 L11 1.5" fill="none" stroke="var(--red)" stroke-width="1.6"/></svg>Just A 30 Days Advance Notice Required</li>
    <li><svg viewBox="0 0 12 12"><rect x="1" y="2" width="9" height="9" fill="none" stroke="var(--red)" stroke-width="1.4"/><path d="M3 6 L5.3 8.4 L11 1.5" fill="none" stroke="var(--red)" stroke-width="1.6"/></svg>You Will Have 12 Months To Complete Travel After Redemption</li>
  </ul>

  <div class="pill how-tag">How can we do this?</div>
  <p class="how-text">We contract with the world leading hotel chains and resorts to help them fill their otherwise empty rooms. We help fill empty rooms which the hotels, resorts and cruise lines turn into additional revenue from other areas of their property and future bookings. Hotels rarely experience full occupancy, yet they remain open, providing rooms and services at fixed costs. So when hotels give out their rooms by partnering with marketing companies like us, they might miss out on the room fee, but they already didn't have that in the first place, at least now they have the opportunity to gain a customer for their in-house restaurants, room service, their casinos, an extra day stay, future bookings, etc.</p>

  <section class="compliments">
    <p class="label">This certificate is<br>compliments of</p>
    <p class="sponsor">Corvane Media</p>
  </section>

  <section class="recipient-box">
    <div class="inner">
      <span class="entry one"></span>
      <span class="entry two"></span>
      <span class="entry three"></span>
      <div class="casino-art" role="img" aria-label="Roulette wheel surrounded by playing cards and casino chips"></div>
    </div>
  </section>

  <footer class="footer">
    <p class="redeem">View all the details of this special offer and redeem online at WWW.TOPAZVOUCHERDESK.COM</p>
    <div class="meta">
      <p class="ids">Certificate ID # 47261-38504<br>Expires 02/29/2020</p>
      <p class="terms">*terms and conditions apply see website for details</p>
    </div>
  </footer>

</main>
</body>
</html>
```